Bold Cover needed for a book on Workplace Bullying

I need a book cover design for a book titled, “Iron Silence?” The book recounts my story of bullying in the workplace. It also includes chapters on how readers can minimize/stop workplace bullying, write an effective complaint, and ensure their own mental wellbeing.
I am looking for a bold design using red and black, and possibly distressed lettering. The covers of other books dealing with this subject do not reflect my vision. They are often too childish or look too academic. This book needs to stress the serious nature of a toxic workplace, while appealing to readers experiencing a similar situation. I’d like the cover to reflect the mental anguish associated with workplace bullying (hence the distressed lettering).
I have included a cover that appeals to me (although the coloring is wrong). That said, I am also very happy (and excited) to see your creative input!
On the cover, it should have the following:
Title: Iron Silence?
Subtitle: How the Harbour Works Department Condones Bullying & Ruins Lives
Author: Owen Frick
Other relevant details:
Book size: 5.5” x 8.5”
Back cover will have a blurb, author picture/short bio, and barcode
The blurb on the back cover reads:
Undermining, intimidation and threats
Despite the Department of Harbour Works allegedly holding a Iron Silence for bullying, these behaviours were an everyday occurrence in at least one workplace. Even after a decade of complaints, numerous witnesses and physical proof, the department failed to act. Instead, they looked the other way, allowing one powerful and well-connected individual to end careers and ruin lives.
After being targeted, one teacher resolved to put an end to the abuse experienced by more than fifty employees. His startling story reveals the relentless bullying, mental health ramifications, and insidious tactics used to cover up the corrosive behaviour.
Those who have experienced a toxic workplace will also find much needed support and guidance, intended to minimise suffering and detail a clear way forward. Chapters include dealing with bullying in the workplace, how to lodge a successful complaint, and how to stay sane during any potential legal action.

```html
<!DOCTYPE html>
<html lang="en">
<head>
<meta charset="utf-8">
<title>Iron Silence – Book Cover</title>
<link href="https://fonts.googleapis.com/css2?family=Anton&family=Oswald:wght@300;700&family=Montserrat:wght@400&display=swap" rel="stylesheet">
<style>
  :root {
    --backdrop: #e6e6e6;
    --cover-red: #dc3129;
    --ink: #0d0b0b;
    --paper: #f2f0ef;
  }
  * { box-sizing: border-box; margin: 0; padding: 0; }
  html, body {
    width: 1200px; height: 800px; overflow: hidden;
    background: var(--backdrop);
  }
  .canvas {
    position: relative; width: 1200px; height: 800px;
    display: flex; align-items: center; justify-content: center;
  }
  .cover {
    position: relative;
    width: 420px; height: 640px;
    background: var(--cover-red);
    border-radius: 3px;
  }
  .title-main {
    position: absolute; left: 58px; top: 72px; width: 315px; height: 140px;
    display: flex; align-items: center; justify-content: center;
    font-family: "Anton", "Impact", sans-serif;
    font-weight: 400; font-size: 150px; line-height: 1; color: var(--ink);
    letter-spacing: 4px;
  }
  .title-band {
    position: absolute; left: 58px; top: 214px; width: 315px; height: 85px;
    background: var(--ink); border-radius: 3px;
    display: flex; align-items: center; justify-content: center;
    font-family: "Anton", "Impact", sans-serif;
    font-size: 68px; line-height: 1; color: var(--paper);
    letter-spacing: 0.5px;
  }
  .subtitle {
    position: absolute; left: 0; right: 0; top: 348px;
    text-align: center; color: var(--paper);
    font-family: "Oswald", "Arial Narrow", sans-serif;
    font-weight: 300; font-size: 31px; line-height: 37px;
  }
  .subtitle .lead { font-weight: 700; }
  .subtitle .emphasis { font-weight: 700; font-style: italic; }
  .author {
    position: absolute; left: 0; right: 0; top: 572px;
    text-align: center; color: var(--paper);
    font-family: "Montserrat", "Helvetica", sans-serif;
    font-size: 27px; letter-spacing: 12px; padding-left: 12px;
  }
</style>
</head>
<body>
<div class="canvas">
  <div class="cover">
    <h1 class="title-main">IRON</h1>
    <div class="title-band">SILENCE?</div>
    <p class="subtitle">
      <span class="lead">How</span><br>
      the Harbour Works Department<br>
      Condones Bullying<br>
      <span class="emphasis">&amp; Ruins Lives</span>
    </p>
    <p class="author">OWEN FRICK</p>
  </div>
</div>
</body>
</html>
```